Make my current Presentation more Professional

I am selling frozen pulp and sorbets. I have a presentation done to introduce the product to customers i want to sell my product to. However the presentation does not have a character - i need to make it look more professional, and at the same time i want to make the product stand out, and have the overall presentation look very fresh, and embedding the true look and feel of what we are offering. 100% NATURAL TROPICAL BRAZILIAN FRUITS.
Some of the text in the presentation is pasted like image, i need it as text.
There should be a specific template that you will use so that i can add remove slides later on according to my requirement

Target Market(s)

Presentation is intended for F&B managers & Chefs in hotels, restaurant

Industry/Entity Type

Food Service

Font styles to use
Sans Serif

Colors

Designer to choose colors to be used in the design.

Requirements
Must have
• A fresh, natural look and feel of tropical fruits.
• It also should come across professional as we are selling products to potential customers.
• I need a clear template - with header, font etc..
Nice to have
• If you want to buy some pictures of fruits, i can buy it for you to make it look great

```html
<!DOCTYPE html>
<html lang="en">
<head>
<meta charset="utf-8">
<title>Pomar Verde — Presentation Template</title>
<link rel="stylesheet" href="https://fonts.googleapis.com/css2?family=Raleway:wght@400;600;700;800&family=Open+Sans:wght@400;600&display=swap">
<style>
:root{
  --green:#1e8a3a;
  --green-dark:#156b2c;
  --yellow:#f2c200;
  --ink:#222;
  --text:#555;
  --canvas:#efefef;
  --white:#fff;
}
*{box-sizing:border-box;margin:0;padding:0}
html,body{width:1144px;height:1200px;overflow:hidden;background:var(--canvas)}
body{position:relative;font-family:"Open Sans",Arial,sans-serif;color:var(--text)}
.slide{position:absolute;background:var(--white);overflow:hidden;box-shadow:0 1px 3px rgba(0,0,0,.08)}
.slide--large{width:524px;height:293px;top:25px}
.slide--small{width:346px;height:194px}
.photo{position:absolute}
.heading{font-family:"Raleway",Arial,sans-serif;font-weight:700;color:var(--ink);line-height:1.15}
.accent{color:var(--green)}
.body{font-size:5px;line-height:1.5;color:var(--text)}
.brand{position:absolute;display:flex;align-items:center;gap:4px;font-family:"Raleway",Arial,sans-serif;font-weight:800;color:var(--green)}
.brand__dot{border-radius:50%;background:var(--green)}
.brand--small{top:9px;right:10px;font-size:9px}
.brand--small .brand__dot{width:9px;height:9px}
.brand--light{color:var(--white)}
.brand--light .brand__dot{background:var(--white)}
.footer-tag{position:absolute;left:0;bottom:0;height:9px;padding:0 12px 0 5px;background:var(--green);color:var(--white);font-size:3.6px;line-height:9px;clip-path:polygon(0 0,88% 0,100% 100%,0 100%)}
.page-num{position:absolute;right:8px;bottom:6px;font-size:7px;color:#777}
.underline{display:block;width:16px;height:2px;background:var(--yellow);margin:4px auto 0}
.cover-title{position:absolute;text-align:right;font-family:"Raleway",Arial,sans-serif;font-weight:800;line-height:1.1}
.cover-title .accent{font-size:17px}
.cover-title .dark{font-size:18px;color:var(--ink)}
.cover-lede{font-family:"Open Sans",Arial,sans-serif;font-weight:400;font-size:8.5px;color:#444;line-height:1.35;margin-top:6px}
.value{position:absolute;top:70px;width:60px;text-align:center;font-size:5.5px;font-weight:600;color:#333}
.value__ring{width:40px;height:40px;margin:0 auto 6px;border-radius:50%;background:var(--green);border:2px solid #fff;box-shadow:0 0 0 1.5px var(--green);display:flex;align-items:center;justify-content:center}
.sub{font-family:"Raleway",Arial,sans-serif;font-weight:700;font-size:6px;color:var(--ink);margin-bottom:3px}
.sub--green{color:var(--green)}
</style>
</head>
<body>

<!-- Cover A -->
<section class="slide slide--large" style="left:31px">
  <svg class="photo" width="524" height="293" viewBox="0 0 524 293">
    <defs><linearGradient id="fruitA" x1="0" y1="0" x2="1" y2="1"><stop offset="0" stop-color="#e9e3c4"/><stop offset=".45" stop-color="#b5c65a"/><stop offset=".75" stop-color="#e8c33a"/><stop offset="1" stop-color="#8a5a2b"/></linearGradient></defs>
    <path role="img" aria-label="Basket of grapes, peaches and bananas" d="M0 0H524V150C420 195 250 220 0 205Z" fill="url(#fruitA)"/>
    <path d="M0 205C250 220 420 195 524 150" fill="none" stroke="var(--green)" stroke-width="7"/>
  </svg>
  <div class="brand" style="left:32px;bottom:25px;font-size:20px"><span class="brand__dot" style="width:18px;height:18px"></span>Pomar Verde</div>
  <div class="cover-title" style="right:16px;top:202px">
    <div class="accent">BUSINESS</div>
    <div class="dark">POWERPOINT TEMPLATE</div>
    <p class="cover-lede">Lorem ipsum dolor sit amet, per ea malis soluta sensibus, no<br>eripuit temporibus vix, qui et modo necessitatibus.</p>
  </div>
</section>

<!-- Cover B -->
<section class="slide slide--large" style="left:572px">
  <svg class="photo" width="524" height="293" viewBox="0 0 524 293">
    <defs><linearGradient id="fruitB" x1="0" y1="0" x2="1" y2="1"><stop offset="0" stop-color="#e9e3c4"/><stop offset=".4" stop-color="#b5c65a"/><stop offset=".7" stop-color="#e8c33a"/><stop offset="1" stop-color="#8a5a2b"/></linearGradient></defs>
    <path role="img" aria-label="Basket of grapes, peaches and bananas on a table" d="M0 0H340C300 40 240 140 240 293H0Z" fill="url(#fruitB)"/>
    <path d="M340 0C300 40 240 140 240 293" fill="none" stroke="var(--green)" stroke-width="6"/>
  </svg>
  <div class="brand" style="right:16px;top:110px;font-size:20px"><span class="brand__dot" style="width:18px;height:18px"></span>Pomar Verde</div>
  <div class="cover-title" style="right:16px;top:146px">
    <div class="accent">BUSINESS</div>
    <div class="dark">POWERPOINT TEMPLATE</div>
    <p class="cover-lede">Lorem ipsum dolor sit amet, per ea malis soluta sensibus, no<br>eripuit temporibus vix, qui et modo necessitatibus.</p>
  </div>
</section>

<!-- About -->
<section class="slide slide--small" style="left:24px;top:341px">
  <div class="photo" role="img" aria-label="Market stall with apples, melons and bananas" style="left:0;top:0;width:180px;height:194px;background:linear-gradient(135deg,#6a3a1e,#c33a2a 45%,#d9a13a 75%,#5a4a2a)"></div>
  <div class="brand brand--small"><span class="brand__dot"></span>Pomar Verde</div>
  <div class="heading" style="position:absolute;left:180px;top:40px;width:166px;height:42px;background:var(--green);color:#fff;font-size:10.5px;padding:8px 10px">About<br>Pomar Verde</div>
  <div class="body" style="position:absolute;left:190px;top:92px;width:146px">
    <p>Pomar Verde fruit pulp is <b>100% made of selected tropical fruit</b>, processed at the optimal stage of ripeness according to a simple but accurate production process. <b>No sugar, preservatives or colorings are added.</b></p>
    <p style="margin-top:5px">The exceptional nutritional qualities of Brazilian fresh fruits are maintained almost unchanged. Thus all drinks, sorbets and power bowls based on our pulps are ideal to prepare excellent juices and vitamins, a daily complement to everybody's diet.</p>
  </div>
</section>

<!-- Wellness -->
<section class="slide slide--small" style="left:399px;top:341px">
  <div class="photo" role="img" aria-label="Bowl of strawberries and blueberries" style="left:170px;top:-30px;width:250px;height:250px;border-radius:50%;background:radial-gradient(circle at 45% 55%,#d2232a,#a8141c 45%,#2a2d5a 75%,#1a1a3a)"></div>
  <div class="brand brand--small brand--light"><span class="brand__dot"></span>Pomar Verde</div>
  <div class="heading" style="position:absolute;left:16px;top:72px;font-size:13px">The Fruits<br><span class="accent">Of Wellness</span></div>
  <p class="body" style="position:absolute;left:16px;top:108px;width:160px">Discover the unique taste of the best tropical fruits from South America. With our pulps you can prepare smoothies, vitamins and all the fruit specialities enjoyed with the new and fascinating exotic varieties that contain numerous and extra ordinary healing properties.</p>
  <div class="footer-tag">100% Natural Tropical Brazilian Fruits</div>
  <span class="page-num" style="color:#fff">2</span>
</section>

<!-- Heading text -->
<section class="slide slide--small" style="left:774px;top:341px">
  <div class="photo" role="img" aria-label="Pile of fresh oranges" style="left:0;top:0;width:346px;height:60px;background:linear-gradient(90deg,#e07a10,#f59a1e 40%,#2f6a20 60%,#f08a15)"></div>
  <div class="brand brand--small brand--light"><span class="brand__dot"></span>Pomar Verde</div>
  <div class="heading" style="position:absolute;top:72px;width:100%;text-align:center;font-size:10px">Heading Text<span class="underline"></span></div>
  <p class="body" style="position:absolute;left:14px;top:98px;width:150px">Pomar Verde was brought to the region by <b>Norte Holding Ltd</b> as master franchisee with the objective of making the products available to customers through shops and retailing of the pulps. The first rights to open shops in the region were granted to Solara Trading Co., registered in the city.</p>
  <p class="body" style="position:absolute;left:182px;top:98px;width:152px"><b>Solara Trading Co.</b> opened their first store in February 2014. The concept is based on Brazilian frozen exotic fruit pulps which are 100% natural without preservatives or colorants, for preparing tasty vitamins, sorbets and famous acai bowls. This wide variety of fruit pulps carries premium characteristics, nutritional value and a high quality of flavour and color.</p>
  <span class="page-num">2</span>
</section>

<!-- Locations -->
<section class="slide slide--small" style="left:24px;top:555px">
  <div class="brand brand--small"><span class="brand__dot"></span>Pomar Verde</div>
  <div class="photo" role="img" aria-label="Food truck outside a shop" style="left:24px;top:31px;width:64px;height:64px;background:linear-gradient(135deg,#4a5a40,#8a9a80)"></div>
  <div class="photo" role="img" aria-label="Shop front with signage" style="left:92px;top:31px;width:64px;height:64px;background:linear-gradient(135deg,#2a3a30,#6a5a40)"></div>
  <div class="photo" role="img" aria-label="Meeting with customers" style="left:24px;top:99px;width:64px;height:63px;background:linear-gradient(135deg,#5a5a50,#b0a890)"></div>
  <div class="photo" role="img" aria-label="Shop counter interior" style="left:92px;top:99px;width:64px;height:63px;background:linear-gradient(135deg,#3a3a30,#8a7a60)"></div>
  <div class="heading" style="position:absolute;left:174px;top:58px;font-size:11.5px;font-weight:600">Our<br>Locations<span class="underline" style="margin:4px 0 0"></span></div>
  <p class="body" style="position:absolute;left:174px;top:96px;width:150px">We are located in the prestigious area of Harbour Walk, close to new cinemas with a view of the majestic beachfront of Bay Shore. Our newest shop is in the Lakeside Clinic. We also have a food truck in Palm Beach.</p>
  <div class="footer-tag">100% Natural Tropical Brazilian Fruits</div>
  <span class="page-num">2</span>
</section>

<!-- Vision / Mission -->
<section class="slide slide--small" style="left:399px;top:555px">
  <svg class="photo" width="160" height="194" viewBox="0 0 160 194">
    <defs><linearGradient id="grapes" x1="0" y1="0" x2="1" y2="1"><stop offset="0" stop-color="#2a5a1e"/><stop offset=".5" stop-color="#5a8a2a"/><stop offset="1" stop-color="#1e3a14"/></linearGradient></defs>
    <polygon role="img" aria-label="Green grapes on the vine" points="0,0 105,0 150,97 105,194 0,194" fill="url(#grapes)"/>
    <polyline points="112,0 157,97 112,194" fill="none" stroke="var(--green)" stroke-width="4"/>
  </svg>
  <div class="brand brand--light" style="left:20px;top:88px;font-size:14px"><span class="brand__dot" style="width:13px;height:13px"></span>Pomar Verde</div>
  <div style="position:absolute;left:174px;top:36px;width:160px">
    <div class="heading accent" style="font-size:10px">VISION</div>
    <p class="body" style="margin-top:4px">To become the number one company providing high quality fruit pulps, vitamins, sorbets &amp; gelato.</p>
    <div class="heading accent" style="font-size:10px;margin-top:16px">MISION</div>
    <p class="body" style="margin-top:4px">To continuously provide consistent quality with utmost customer satisfaction and services while bearing in mind exceeding their expectations at all times, combined with employee motivation, training and good team spirit.</p>
  </div>
  <span class="page-num">2</span>
</section>

<!-- Values -->
<section class="slide slide--small" style="left:774px;top:555px">
  <div class="photo" role="img" aria-label="Faded strawberries, lemons and berries" style="inset:0;background:linear-gradient(135deg,#f6e3e3,#fbf6e0 45%,#fbf3d6 65%,#e3e6f0)"></div>
  <div class="brand brand--small"><span class="brand__dot"></span>Pomar Verde</div>
  <div class="heading" style="position:absolute;top:40px;width:100%;text-align:center;font-size:10px">Our Values<span class="underline"></span></div>
  <div class="value" style="left:10px"><div class="value__ring"><svg width="18" height="18" viewBox="0 0 18 18" fill="none" stroke="#fff" stroke-width="1.3"><circle cx="9" cy="9" r="8"/><circle cx="9" cy="9" r="5"/><circle cx="9" cy="9" r="2"/></svg></div>Customer<br>Focus</div>
  <div class="value" style="left:74px"><div class="value__ring"><svg width="18" height="18" viewBox="0 0 18 18" fill="none" stroke="#fff" stroke-width="1.3"><circle cx="9" cy="9" r="7.5"/><path d="M5.5 10.5q3.5 3.5 7 0"/><circle cx="6.5" cy="7" r=".6" fill="#fff"/><circle cx="11.5" cy="7" r=".6" fill="#fff"/></svg></div>Happy</div>
  <div class="value" style="left:138px"><div class="value__ring"><svg width="18" height="18" viewBox="0 0 18 18" fill="none" stroke="#fff" stroke-width="1.3"><circle cx="9" cy="6" r="2.5"/><path d="M4 15q5-7 10 0"/><circle cx="4" cy="8" r="1.6"/><circle cx="14" cy="8" r="1.6"/></svg></div>Teamwork</div>
  <div class="value" style="left:202px"><div class="value__ring"><svg width="18" height="18" viewBox="0 0 18 18" fill="none" stroke="#fff" stroke-width="1.3"><path d="M9 15S2 10.5 2 6.5A3.5 3.5 0 0 1 9 5a3.5 3.5 0 0 1 7 1.5C16 10.5 9 15 9 15Z"/></svg></div>Integrity</div>
  <div class="value" style="left:266px"><div class="value__ring"><svg width="18" height="18" viewBox="0 0 18 18" fill="none" stroke="#fff" stroke-width="1.3"><path d="M10 1 4 10h5l-1 7 6-9H9Z"/></svg></div>Energy</div>
  <div class="footer-tag">100% Natural Tropical Brazilian Fruits</div>
  <span class="page-num">2</span>
</section>

<!-- Carts -->
<section class="slide slide--small" style="left:24px;top:769px">
  <div class="brand brand--small"><span class="brand__dot"></span>Pomar Verde</div>
  <div class="photo" role="img" aria-label="Fruit kiosk cart with striped awning" style="left:8px;top:8px;width:86px;height:76px;background:linear-gradient(160deg,#f3f3f3,#c9b89a 50%,#9a6a3a)"></div>
  <div class="photo" role="img" aria-label="Sorbet serving cart" style="left:98px;top:74px;width:82px;height:82px;background:linear-gradient(160deg,#f3f3f3,#e9a04a 40%,#b8bcbf)"></div>
  <div class="heading" style="position:absolute;left:208px;top:60px;font-size:11.5px;font-weight:600">Your<br>Text Here<span class="underline" style="margin:4px 0 0"></span></div>
  <p class="body" style="position:absolute;left:208px;top:100px;width:126px">Qui et modo necessitatibus. Vix cu wisi assentior, ut quo debet ullamcorper, ei nam quas albucius. Scripta mentis comprehensam eum no, harum indoctum cu his. Cu vim quando omnesque consulatu, te solum quaque incorrupte vim, possit laoreet prodesset vis id.</p>
  <div class="footer-tag">100% Natural Tropical Brazilian Fruits</div>
  <span class="page-num">2</span>
</section>

<!-- Bowls -->
<section class="slide slide--small" style="left:399px;top:769px">
  <div class="photo" role="img" aria-label="Acai bowl topped with fruit and honey" style="left:0;top:0;width:93px;height:194px;background:linear-gradient(180deg,#e9d9a0,#f0b020 20%,#c24a30 50%,#9a6a3a 75%,#e6e0d0)"></div>
  <div class="photo" role="img" aria-label="Sliced watermelon" style="left:175px;top:0;width:89px;height:194px;background:linear-gradient(160deg,#3a6a2a,#e0423a 35%,#c82a2a 70%,#7a5a3a)"></div>
  <div style="position:absolute;left:100px;top:42px;width:70px">
    <div class="heading" style="font-size:8.5px">Super Bowls Frutta acai na tigela</div>
    <p class="body" style="margin-top:6px">A Brazilian speciality made from acai, banana and cereals, which is a meal substitute. Choose to add honey along with two toppings from peanuts, cashews, walnuts, almonds or chocolate.</p>
  </div>
  <div style="position:absolute;left:271px;top:42px;width:70px">
    <div class="heading" style="font-size:8.5px">Fresh Watermelon Sliced</div>
    <p class="body" style="margin-top:6px">Qui et modo necessitatibus. Vix cu wisi assentior, ut quo debet ullamcorper, ei nam quas albucius. Scripta mentis comprehensam eum no, harum indoctum cu his. Cu vim quando omnesque consulatu, te solum quaque incorrupte vim, possit laoreet prodesset vis id.</p>
  </div>
</section>

<!-- Diamonds -->
<section class="slide slide--small" style="left:774px;top:769px">
  <svg class="photo" width="346" height="194" viewBox="0 0 346 194" role="img" aria-label="Oranges with leaves in a diamond mosaic">
    <defs><linearGradient id="orange" x1="0" y1="0" x2="1" y2="1"><stop offset="0" stop-color="#f59a1e"/><stop offset=".5" stop-color="#e0700e"/><stop offset=".7" stop-color="#3a6a20"/><stop offset="1" stop-color="#f08a15"/></linearGradient></defs>
    <polygon points="150,60 210,0 346,0 346,194 230,194 150,114" fill="url(#orange)"/>
    <g stroke="#fff" stroke-width="2.5" fill="none">
      <line x1="150" y1="60" x2="284" y2="194"/><line x1="210" y1="0" x2="346" y2="136"/><line x1="270" y1="0" x2="346" y2="76"/>
      <line x1="150" y1="114" x2="264" y2="0"/><line x1="200" y1="194" x2="346" y2="48"/><line x1="260" y1="194" x2="346" y2="108"/>
    </g>
    <polygon points="150,60 210,0 150,0" fill="#fff"/><polygon points="150,114 230,194 150,194" fill="#fff"/>
  </svg>
  <div class="heading" style="position:absolute;left:20px;top:72px;font-size:11.5px;font-weight:600">Your<br>Text Here<span class="underline" style="margin:4px 0 0"></span></div>
  <p class="body" style="position:absolute;left:20px;top:110px;width:130px">Qui et modo necessitatibus. Vix cu wisi assentior, ut quo debet ullamcorper, ei nam quas albucius. Scripta mentis comprehensam eum no, harum indoctum cu his. Cu vim quando omnesque consulatu, te solum quaque incorrupte vim, possit laoreet prodesset vis id.</p>
  <span class="page-num">2</span>
</section>

<!-- Stripes -->
<section class="slide slide--small" style="left:24px;top:984px">
  <svg class="photo" width="346" height="194" viewBox="0 0 346 194" role="img" aria-label="Peaches and bananas in pill-shaped stripes">
    <defs><linearGradient id="peach" x1="0" y1="0" x2="1" y2="1"><stop offset="0" stop-color="#f0c030"/><stop offset=".3" stop-color="#e8503a"/><stop offset=".7" stop-color="#c8202a"/><stop offset="1" stop-color="#e8703a"/></linearGradient></defs>
    <g fill="url(#peach)" transform="rotate(-4 173 97)">
      <rect x="70" y="2" width="300" height="14" rx="7"/><rect x="40" y="20" width="330" height="14" rx="7"/>
      <rect x="90" y="38" width="280" height="14" rx="7"/><rect x="110" y="56" width="260" height="14" rx="7"/>
      <rect x="140" y="74" width="230" height="14" rx="7"/><rect x="160" y="92" width="210" height="14" rx="7"/>
      <rect x="150" y="110" width="220" height="14" rx="7"/><rect x="180" y="128" width="190" height="14" rx="7"/>
      <rect x="200" y="146" width="170" height="14" rx="7"/><rect x="190" y="164" width="180" height="14" rx="7"/>
    </g>
  </svg>
  <div class="heading" style="position:absolute;left:12px;top:86px;font-size:11.5px;font-weight:600">Your<br>Text Here<span class="underline" style="margin:4px 0 0"></span></div>
  <p class="body" style="position:absolute;left:12px;top:120px;width:120px">Qui et modo necessitatibus. Vix cu wisi assentior, ut quo debet ullamcorper, ei nam quas albucius. Scripta mentis comprehensam eum no, harum indoctum cu his. Cu vim quando omnesque consulatu, te solum quaque incorrupte vim, possit laoreet prodesset vis id.</p>
  <div class="footer-tag">100% Natural Tropical Brazilian Fruits</div>
  <span class="page-num">2</span>
</section>

<!-- Three photos -->
<section class="slide slide--small" style="left:399px;top:984px">
  <div class="heading" style="position:absolute;top:28px;width:100%;text-align:center;font-size:10px">Heading Text<span class="underline"></span></div>
  <div class="photo" role="img" aria-label="Bunches of red and green grapes" style="left:14px;top:58px;width:100px;height:58px;background:linear-gradient(135deg,#3a4a2a,#6a3a4a 50%,#8a9a5a)"></div>
  <div class="photo" role="img" aria-label="Oranges on the branch" style="left:124px;top:58px;width:100px;height:58px;background:linear-gradient(135deg,#e07a10,#f5a020 50%,#3a6a20)"></div>
  <div class="photo" role="img" aria-label="Basket of mixed fruit" style="left:234px;top:58px;width:100px;height:58px;background:linear-gradient(135deg,#e9e3c4,#b5c65a 50%,#e8c33a)"></div>
  <div style="position:absolute;left:18px;top:124px;width:94px"><div class="sub">Heading Text</div><p class="body">Qui et modo necessitatibus. Vix cu wisi assentior, ut quo debet ullamcorper, ei nam quas albucius.</p></div>
  <div style="position:absolute;left:128px;top:124px;width:94px"><div class="sub">Heading Text</div><p class="body">Qui et modo necessitatibus. Vix cu wisi assentior, ut quo debet ullamcorper, ei nam quas albucius.</p></div>
  <div style="position:absolute;left:238px;top:124px;width:94px"><div class="sub">Heading Text</div><p class="body">Qui et modo necessitatibus. Vix cu wisi assentior, ut quo debet ullamcorper, ei nam quas albucius.</p></div>
  <div class="footer-tag">100% Natural Tropical Brazilian Fruits</div>
  <span class="page-num">2</span>
</section>

<!-- Circle -->
<section class="slide slide--small" style="left:774px;top:984px">
  <div class="brand brand--small"><span class="brand__dot"></span>Pomar Verde</div>
  <div class="photo" role="img" aria-label="Bunch of bananas on a yellow background" style="left:115px;top:38px;width:116px;height:116px;border-radius:50%;background:radial-gradient(circle at 50% 50%,#f7e04a,#f0c010 60%,#e8b000)"></div>
  <div style="position:absolute;left:26px;top:40px;width:80px"><div class="sub sub--green">Heading Text</div><p class="body">Qui et modo necessitatibus. Vix cu wisi assentior, ut quo debet ullamcorper, ei nam quas albucius.</p></div>
  <div style="position:absolute;left:26px;top:102px;width:80px"><div class="sub sub--green">Heading Text</div><p class="body">Qui et modo necessitatibus. Vix cu wisi assentior, ut quo debet ullamcorper, ei nam quas albucius.</p></div>
  <div style="position:absolute;left:240px;top:40px;width:80px"><div class="sub sub--green">Heading Text</div><p class="body">Qui et modo necessitatibus. Vix cu wisi assentior, ut quo debet ullamcorper, ei nam quas albucius.</p></div>
  <div style="position:absolute;left:240px;top:102px;width:80px"><div class="sub sub--green">Heading Text</div><p class="body">Qui et modo necessitatibus. Vix cu wisi assentior, ut quo debet ullamcorper, ei nam quas albucius.</p></div>
  <div class="footer-tag">100% Natural Tropical Brazilian Fruits</div>
  <span class="page-num">2</span>
</section>

</body>
</html>
```